Wellmere Talking Therapies House

We need a design for magazine advert, ideally high resolution to advertise our counselling centre. we would like this to include a photo of two people talking, as if in a counselling session. See our logo and colour range on our website. www.wellmere-house.co.uk
The photo should not include cups of coffee, clipboards, desks, people touching. it needs to be two people in armchairs sympathetically listening and looking at each other.
The font type is Great Vibes on the logo. Our design should communicate a centre of excellence delivering high quality, professional services in stylishly furnished surroundings.
Updates

Hello Everyone We have had a number of designs that look quite promising but are missing the brief. Can I reiterate that we need a photograph of 2 people seated talking to each other in a sincere way. There shouldn't be office chairs but comfortable chairs. There should be no physical contact. There should be no clipboards.Thank you very muchHeather Added Sunday, March 12, 2017

Target Market(s)

people seeking counselling and psychotherapy

Font styles to use
Other font styles liked:
• Great Vibes as in our logo for some of the print. See attached file.

Requirements
Must have
• good photograph
• Two high res Pixelvane photos:
• https://pixelvane-files.example-portal.net/download/photo-one-ref-7341
• https://pixelvane-files.example-portal.net/download/photo-two-ref-9826
Nice to have
• Watermark in keeping with our logo.
Should not have
• Darkness

```html
<!DOCTYPE html>
<html lang="en">
<head>
<meta charset="utf-8">
<title>Wellmere Talking Therapies House – Advert</title>
<link rel="stylesheet" href="https://fonts.googleapis.com/css2?family=Great+Vibes&family=Open+Sans:wght@400&family=Roboto+Condensed:wght@700&display=swap">
<style>
  :root {
    --backdrop: #eceeec;
    --paper-top: #f4f4f5;
    --paper-bottom: #e6e6e8;
    --olive: #8a8c0e;
    --olive-dark: #4d4f0a;
    --ink: #111111;
    --text-olive: #3f4209;
    --white: #ffffff;
  }
  * { margin: 0; padding: 0; box-sizing: border-box; }
  html, body { width: 1200px; height: 1200px; overflow: hidden; }
  body { background: var(--backdrop); position: relative; font-family: "Open Sans", Arial, sans-serif; }

  .advert {
    position: absolute; left: 200px; top: 40px; width: 800px; height: 1120px;
    background: linear-gradient(180deg, var(--paper-top), var(--paper-bottom));
    box-shadow: 0 6px 18px rgba(0,0,0,0.18);
    overflow: hidden;
  }
  .hero { position: absolute; left: 0; top: 0; width: 800px; height: 640px; }

  .brand {
    position: absolute; left: 440px; top: 480px; width: 330px; text-align: center;
  }
  .brand-mark {
    width: 46px; height: 46px; border-radius: 50%;
    background: var(--olive); margin: 0 auto 8px;
  }
  .brand-name {
    font-family: "Great Vibes", cursive; font-size: 32px; line-height: 1.05;
    color: var(--olive-dark);
  }

  .quote {
    position: absolute; left: 76px; top: 628px; width: 680px;
    color: var(--text-olive); font-size: 26px; line-height: 35px;
  }
  .quote-text { padding-left: 20px; }
  .quote-mark { position: absolute; font-family: Georgia, serif; font-style: italic; font-size: 44px; color: var(--ink); }
  .quote-mark.open { left: 0; top: -8px; }
  .quote-mark.close { right: 10px; top: 46px; }
  .quote-author { text-align: right; padding-right: 44px; font-size: 16px; line-height: 22px; }

  .headline {
    position: absolute; left: 0; top: 728px; width: 800px; text-align: center;
    font-family: "Great Vibes", cursive; font-weight: 700; color: var(--ink);
    font-size: 50px; line-height: 53px;
    text-shadow: 0.6px 0 0 var(--ink);
  }
  .headline .small { font-size: 40px; }

  .intro {
    position: absolute; left: 80px; top: 907px; width: 680px;
    color: var(--text-olive); font-size: 18.5px; line-height: 26px;
  }
  .availability {
    position: absolute; left: 0; top: 970px; width: 800px; text-align: center;
    font-family: "Roboto Condensed", "Arial Narrow", sans-serif; font-weight: 700;
    font-size: 29px; color: var(--ink);
  }

  .contact-band {
    position: absolute; left: 22px; top: 1022px; width: 746px; height: 84px;
    background: var(--olive); color: var(--white);
  }
  .contact-phone { position: absolute; left: 0; top: 8px; width: 100%; text-align: center; font-size: 23px; }
  .contact-web { position: absolute; left: 36px; top: 48px; font-size: 18px; }
  .contact-address { position: absolute; right: 30px; top: 50px; font-size: 18px; }
</style>
</head>
<body>
  <main class="advert">
    <svg class="hero" viewBox="0 0 800 640" aria-hidden="false">
      <defs>
        <linearGradient id="photoTone" x1="0" y1="0" x2="1" y2="1">
          <stop offset="0" stop-color="#e9dcd6"/>
          <stop offset="0.5" stop-color="#f1e6e2"/>
          <stop offset="1" stop-color="#c9d6e6"/>
        </linearGradient>
      </defs>
      <path class="hero-shadow" d="M0 540 Q140 612 270 606 Q560 560 800 40 L800 60 Q560 580 270 616 Q130 620 0 556 Z" fill="#d2d2d4"/>
      <path class="hero-photo" role="img" aria-label="Photograph of two older people seated, smiling and talking to each other"
            d="M0 265 Q250 20 650 0 L800 0 L800 50 Q560 560 270 600 Q130 606 0 532 Z" fill="url(#photoTone)"/>
      <path class="hero-arc" d="M0 265 Q250 20 650 0 L690 0 Q260 30 0 282 Z" fill="var(--olive)"/>
    </svg>

    <div class="brand">
      <div class="brand-mark"></div>
      <div class="brand-name">Wellmere Talking Therapies House</div>
    </div>

    <blockquote class="quote">
      <span class="quote-mark open">“</span>
      <p class="quote-text">A big port of letting go is recognising when it is time to stay in a situation and when it is time to move on.</p>
      <span class="quote-mark close">”</span>
      <p class="quote-author">- Elspeth R. Marlowe</p>
    </blockquote>

    <h1 class="headline">Confidential Therapeutic Services<br><span class="small">in the</span><br>Heart of Old Town</h1>

    <p class="intro">We have over 30 carefully selected, qualified and professional therapists offering a range of services to help individuals, families and couples.</p>

    <p class="availability">Appointments available Throughout the day and evening</p>

    <footer class="contact-band">
      <p class="contact-phone">CALL: 01632 960418</p>
      <p class="contact-web">www.wellmere-house.co.uk</p>
      <p class="contact-address">14 Linden Row, Old Town, Brackford BR2 7QE</p>
    </footer>
  </main>
</body>
</html>
```